Book Cover - Biography of Terrell and Joanne Whitfield

I am writing a biography about Terrell and Joanne Whitfield. I need a book cover designed for this. The title of the book is: Harvest of Courage: Terrell and Joanne Whitfield. I need one version for Ebook with size of 2000px wide by 3200px high and one version for audiobook with size of 3200px wide by 3200px high. *NOTE: Please only use non-copywrite images (open source / royalty-free.)

```html
<!DOCTYPE html>
<html lang="en">
<head>
<meta charset="utf-8">
<title>Harvest of Courage: Terrell and Joanne Whitfield — Cover Set</title>
<link rel="stylesheet" href="https://fonts.googleapis.com/css2?family=Crimson+Pro:wght@400&display=swap">
<style>
  :root {
    --stage: #a0a0a0;
    --paper: #ffffff;
    --paper-soft: #f3f3f3;
    --band-dark: #1c1516;
    --band-warm: #5a3a30;
    --band-accent: #c41a3c;
    --charcoal: #363537;
    --title: #ffffff;
  }
  html, body {
    margin: 0;
    width: 1200px;
    height: 1200px;
    overflow: hidden;
    background: var(--stage);
  }
  .cover-set {
    position: relative;
    width: 1200px;
    height: 1200px;
  }
  .cover {
    position: absolute;
    display: block;
  }
  .cover--audiobook { left: 119px; top: 405px; width: 484px; height: 456px; }
  .cover--ebook { left: 675px; top: 341px; width: 399px; height: 583px; }
  .cover-title {
    font-family: "Crimson Pro", Georgia, serif;
    font-weight: 400;
    fill: var(--title);
  }
</style>
</head>
<body>
<main class="cover-set">

  <svg class="cover cover--audiobook" viewBox="0 0 484 456" aria-label="Audiobook cover">
    <defs>
      <linearGradient id="portrait-tones-square" x1="0" y1="0" x2="1" y2="0">
        <stop offset="0" stop-color="var(--band-dark)"/>
        <stop offset="0.55" stop-color="#2a1e1d"/>
        <stop offset="0.8" stop-color="var(--band-warm)"/>
        <stop offset="1" stop-color="#6b2a33"/>
      </linearGradient>
    </defs>
    <rect class="cover-paper" width="484" height="456" fill="var(--paper)"/>
    <polygon class="portrait-band" role="img" aria-label="Portrait of Terrell and Joanne Whitfield smiling side by side, posterized style"
      points="0,129 484,2 484,251 0,381" fill="url(#portrait-tones-square)"/>
    <polygon class="charcoal-wedge" points="0,381 484,251 484,456 378,456" fill="var(--charcoal)"/>
    <text class="cover-title" font-size="30">
      <tspan x="26" y="268">Harvest of Courage:</tspan>
      <tspan x="26" y="306">Terrell and Joanne Whitfield</tspan>
    </text>
  </svg>

  <svg class="cover cover--ebook" viewBox="0 0 399 583" aria-label="Ebook cover">
    <defs>
      <linearGradient id="portrait-tones-tall" x1="0" y1="0" x2="1" y2="0">
        <stop offset="0" stop-color="var(--band-dark)"/>
        <stop offset="0.55" stop-color="#2a1e1d"/>
        <stop offset="0.8" stop-color="var(--band-warm)"/>
        <stop offset="1" stop-color="#6b2a33"/>
      </linearGradient>
    </defs>
    <rect class="cover-paper" width="399" height="583" fill="var(--paper)"/>
    <polygon class="soft-facet" points="0,0 106,0 367,77 0,176" fill="var(--paper-soft)"/>
    <polygon class="portrait-band" role="img" aria-label="Portrait of Terrell and Joanne Whitfield smiling side by side, posterized style"
      points="0,176 399,69 399,282 0,388" fill="url(#portrait-tones-tall)"/>
    <polygon class="charcoal-wedge" points="0,388 399,322 399,583 303,583 0,478" fill="var(--charcoal)"/>
    <text class="cover-title" font-size="28">
      <tspan x="42" y="419">Harvest of Courage:</tspan>
      <tspan x="42" y="453">Terrell and Joanne Whitfield</tspan>
    </text>
  </svg>

</main>
</body>
</html>
```